Update New Business Card - For Start Up

I need to update my business card, I have our old version for example. I would like to keep to the same colors and theme. We are a threat reporting and case management tool for corporations and educational institutions.

Target Market(s)

Corporate Security and Human Resources, School Administrators and Superintendents.

Industry/Entity Type

Physical Security and Technology.

Contact Information for Business Card

My Name, Founder/CEO, phone number 555-214-6082, Logo, Web...

Colors
0054AA
0677BA
7BADD7
CADEEF
E8F1F8

Requirements
Must have
• Something new and trendy.

```html
<!DOCTYPE html>
<html lang="en">
<head>
<meta charset="UTF-8">
<title>Vantora Business Card</title>
<link rel="stylesheet" href="https://fonts.googleapis.com/css2?family=Montserrat:wght@500;600;700&display=swap">
<style>
  :root {
    --brand-blue: #1f75ba;
    --accent-cyan: #0aa0dc;
    --paper: #ffffff;
    --back-bg: #f3f3f3;
    --watermark: #e8ecf0;
    --ink: #2b2b2b;
    --text-dark: #333333;
  }
  * { margin: 0; padding: 0; box-sizing: border-box; }
  html, body {
    width: 987px; height: 1200px; overflow: hidden;
    background: var(--paper);
    font-family: "Montserrat", Arial, sans-serif;
  }
  .sheet { position: relative; width: 987px; height: 1200px; }

  /* Front side */
  .card-front {
    position: absolute; left: 28px; top: 28px; width: 945px; height: 566px;
    background: var(--brand-blue); overflow: hidden;
  }
  .divider-light {
    position: absolute; left: 469px; width: 6px; background: var(--paper);
  }
  .divider-light.top { top: 0; height: 170px; }
  .divider-light.bottom { top: 395px; height: 171px; }
  .brand-lockup {
    position: absolute; left: 193px; top: 228px; height: 112px;
    display: flex; align-items: center; gap: 38px;
  }
  .brand-dot {
    width: 110px; height: 110px; border-radius: 50%; background: var(--paper);
  }
  .brand-name {
    color: var(--paper); font-weight: 500; font-size: 54px;
    letter-spacing: 9px; line-height: 1;
  }

  /* Back side */
  .card-back {
    position: absolute; left: 28px; top: 622px; width: 945px; height: 566px;
    background: var(--back-bg); overflow: hidden;
  }
  .back-circle {
    position: absolute; left: 189px; top: 0; width: 566px; height: 566px;
    border-radius: 50%; background: var(--watermark);
  }
  .person {
    position: absolute; left: 0; width: 945px; top: 280px; text-align: center;
  }
  .person-name {
    color: var(--brand-blue); font-weight: 700; font-size: 28px; letter-spacing: 0.5px;
  }
  .person-title {
    margin-top: 2px; color: var(--text-dark); font-weight: 600; font-size: 18px;
  }
  .divider-blue {
    position: absolute; left: 469px; top: 395px; width: 5px; height: 171px;
    background: var(--brand-blue);
  }
  .icon {
    position: absolute; width: 34px; height: 34px;
  }
  .contact-line {
    position: absolute; color: var(--ink); font-weight: 500; font-size: 24px; line-height: 1;
  }
</style>
</head>
<body>
<div class="sheet">
  <section class="card-front">
    <div class="divider-light top"></div>
    <div class="divider-light bottom"></div>
    <div class="brand-lockup">
      <div class="brand-dot"></div>
      <span class="brand-name">VANTORA</span>
    </div>
  </section>

  <section class="card-back">
    <div class="back-circle"></div>
    <div class="person">
      <div class="person-name">DANIEL HARLOW</div>
      <div class="person-title">CHIEF EXECUTIVE OFFICER</div>
    </div>
    <div class="divider-blue"></div>

    <svg class="icon" style="left:192px;top:418px" viewBox="0 0 34 34" aria-hidden="true">
      <circle cx="17" cy="17" r="17" fill="var(--accent-cyan)"/>
      <path d="M11 9.5c1-.8 2-.6 2.6.3l1.6 2.6c.5.8.3 1.6-.4 2.1l-1 .7c.7 2 2.3 3.8 4.3 4.8l.8-1c.6-.7 1.4-.8 2.1-.3l2.5 1.7c.9.6.9 1.7.1 2.6-1.4 1.6-3.2 2-5.1 1-4.2-2.1-7.2-5.4-8.6-9.5-.6-2 .1-3.7 1.1-5z" fill="#fff"/>
    </svg>
    <div class="contact-line" style="left:260px;top:406px">888-899-3799</div>
    <div class="contact-line" style="left:260px;top:453px">555-214-6082</div>

    <svg class="icon" style="left:522px;top:402px" viewBox="0 0 34 34" aria-hidden="true">
      <circle cx="17" cy="17" r="17" fill="var(--accent-cyan)"/>
      <rect x="9" y="11" width="16" height="12" rx="1.5" fill="#fff"/>
      <path d="M9.5 12l7.5 6 7.5-6" stroke="var(--accent-cyan)" stroke-width="1.6" fill="none"/>
    </svg>
    <div class="contact-line" style="left:590px;top:408px">www.vantora.co</div>

    <svg class="icon" style="left:522px;top:444px" viewBox="0 0 34 34" aria-hidden="true">
      <circle cx="17" cy="17" r="17" fill="var(--accent-cyan)"/>
      <g fill="none" stroke="#fff" stroke-width="1.4">
        <circle cx="17" cy="17" r="8.5"/>
        <ellipse cx="17" cy="17" rx="3.8" ry="8.5"/>
        <path d="M8.5 17h17M10 12.5h14M10 21.5h14"/>
      </g>
    </svg>
    <div class="contact-line" style="left:588px;top:449px">dan@vantora.co</div>
  </section>
</div>
</body>
</html>
```